pressure washing advertisment

I would like front and back designed post cards. we offer pressure washing services for residential customers. I want to highlight before and after pictures as examples of our more popular services. I would also like to have our email www.brightlanewashco.com and the facebook and Instagram logo somewhere. you can also include all major credit card logos as acceptable payments. I have attached our logo along with before and after pictures. also feel free to go to my website for any additional information that should be added to the post card. lastly I want a small promotion of $25 off any service somewhere.<br/><br/>Thank you!!

Target Market(s)

homeowners

Industry/Entity Type

Cleaning Service

Font styles to use
Serif
Sans Serif

Colors

Designer to choose colors to be used in the design.

Requirements
Must have
• before and after pictures with website and logo
Nice to have
• clean look that flows

```html
<!DOCTYPE html>
<html lang="en">
<head>
<meta charset="utf-8">
<title>Brightlane Wash Co – Postcard</title>
<link rel="stylesheet" href="https://fonts.googleapis.com/css2?family=Oswald:wght@400;500;600;700&family=Lato:wght@400;700&display=swap">
<style>
:root{
  --blue:#1b4f8c;
  --blue-dark:#123d70;
  --blue-bright:#2168b0;
  --red:#e3202a;
  --ink:#1d1d1d;
  --grey-bg:#6b6b6b;
  --white:#ffffff;
  --line:#dcdcdc;
  --stamp:#e8e8e8;
}
*{box-sizing:border-box;margin:0;padding:0}
html,body{width:1200px;height:1200px;overflow:hidden;background:var(--grey-bg)}
body{position:relative;font-family:"Lato",sans-serif;color:var(--ink)}
.card{position:absolute;left:211px;width:778px;height:518px;background:var(--white);overflow:hidden}
.card--front{top:52px}
.card--back{top:622px}
.abs{position:absolute}

/* front */
.headline{font-family:"Oswald",sans-serif;line-height:.98;text-transform:uppercase}
.headline__strong{color:var(--blue);font-weight:700;font-size:38px;letter-spacing:-.3px}
.headline__light{color:var(--ink);font-weight:400;font-size:32px;letter-spacing:-.6px;margin-top:2px}
.brand{display:flex;align-items:center;gap:7px;font-family:"Oswald",sans-serif;font-weight:700;color:var(--blue);text-transform:uppercase;white-space:nowrap}
.brand__dot{width:16px;height:16px;border-radius:50%;background:var(--red);flex:none}
.brand--front{right:32px;top:44px;font-size:23px}
.photo{left:0;top:164px;width:778px;height:280px;background:linear-gradient(180deg,#b9c5d6 0%,#8e9bb0 35%,#7a7672 65%,#c9a77c 85%,#5b6b3e 100%)}
.offer{left:482px;top:120px;width:296px;height:140px;background:linear-gradient(135deg,var(--blue-bright),var(--blue-dark));border-radius:30px 0 0 30px;color:var(--white);font-family:"Oswald",sans-serif}
.offer__amount{position:absolute;left:22px;top:4px;font-size:84px;font-weight:600;letter-spacing:-1px;line-height:1.2}
.offer__amount sup{font-size:38px;vertical-align:top;position:relative;top:18px}
.offer__note{position:absolute;right:30px;top:104px;font-family:"Lato",sans-serif;font-weight:700;font-size:14px}
.feature__ring{width:88px;height:88px;border-radius:50%;background:var(--white);border:5px solid var(--red);display:flex;align-items:center;justify-content:center;transform:translate(-50%,-50%)}
.feature__label{transform:translateX(-50%);height:24px;padding:0 11px;background:var(--red);color:var(--white);border-radius:12px;border:2px solid var(--white);box-shadow:0 1px 3px rgba(0,0,0,.25);font-family:"Oswald",sans-serif;font-weight:500;font-size:10.5px;line-height:20px;text-transform:uppercase;white-space:nowrap}
.contact-row{left:0;top:476px;width:778px;display:flex;align-items:center;justify-content:space-between;padding:0 30px;font-size:14.5px}
.contact-row__item{display:flex;align-items:center;gap:7px}
.contact-row__sep{width:2px;height:20px;background:var(--blue)}

/* back */
.back-left{left:0;top:0;width:411px;height:518px}
.strip{left:0;top:0;width:25px;height:518px;background:var(--blue)}
.gallery-band{left:0;top:222px;width:397px;height:132px;background:linear-gradient(90deg,var(--blue-bright),var(--blue-dark));border-radius:0 24px 24px 0}
.panel-top{left:25px;top:0;width:386px;height:222px;background:var(--white);border-radius:0 0 0 24px}
.panel-bottom{left:25px;top:354px;width:386px;height:164px;background:var(--white);border-radius:24px 0 0 0}
.ribbon{left:19px;height:24px;padding:0 16px 0 18px;background:var(--red);border-radius:0 12px 12px 0;color:var(--white);font-family:"Oswald",sans-serif;font-weight:500;font-size:15.5px;line-height:24px;text-transform:uppercase;white-space:nowrap}
.services{display:grid;grid-template-columns:200px 200px;row-gap:4px;font-size:11.3px;left:33px}
.services li{list-style:none;position:relative;padding-left:9px}
.services li::before{content:"";position:absolute;left:0;top:5px;width:5px;height:5px;border-radius:50%;background:var(--red)}
.shot{border-radius:50%;border:4px solid var(--red);box-shadow:0 0 0 2px var(--white);transform:translate(-50%,-50%)}
.shot--before{width:64px;height:64px}
.shot--after{width:77px;height:77px}
.tag{height:16px;padding:0 7px;background:var(--red);color:var(--white);border-radius:8px;font-family:"Lato",sans-serif;font-weight:700;font-style:italic;font-size:11px;line-height:16px}
.back-contact{left:41px;font-size:11px;display:flex;align-items:center;gap:6px}
.brand--back{left:236px;top:456px;font-size:15px;gap:6px}
.divider{left:411px;top:0;width:6px;height:518px;background:linear-gradient(90deg,rgba(0,0,0,.12),rgba(0,0,0,0))}
.mail-address{left:446px;top:90px;display:flex;gap:6px;font-size:9.5px;line-height:12px}
.stamp{left:670px;top:49px;width:68px;height:71px;background:var(--stamp)}
.address-line{left:459px;width:280px;height:1px;background:var(--line)}
</style>
</head>
<body>

<section class="card card--front" aria-label="Postcard front">
  <div class="abs photo" role="img" aria-label="Photo of a two-storey grey-sided family home at dusk with warm lit windows"></div>

  <div class="abs headline" style="background:var(--white);left:0;top:0;width:778px;height:164px;padding:18px 0 0 29px">
    <div class="headline__strong">Professional Residential</div>
    <div class="headline__strong">&amp; Commercial</div>
    <div class="headline__light">Pressure Washing Contractor</div>
    <div class="headline__light">In St. Augustine, FL</div>
  </div>

  <div class="abs brand brand--front"><span class="brand__dot"></span>Brightlane Wash Co</div>

  <div class="abs offer">
    <div class="offer__amount"><sup>$</sup>25 OFF</div>
    <div class="offer__note">ON ANY SERVICE OFFER</div>
  </div>

  <div class="abs feature__ring" style="left:119px;top:378px">
    <svg width="40" height="34" viewBox="0 0 40 34"><path d="M20 3C10 3 3 9 3 16c0 4 2 7 5 9l-2 6 7-4c2 1 5 1 7 1 10 0 17-6 17-12S30 3 20 3z" fill="none" stroke="var(--red)" stroke-width="3"/><circle cx="13" cy="16" r="2.3" fill="var(--red)"/><circle cx="20" cy="16" r="2.3" fill="var(--red)"/><circle cx="27" cy="16" r="2.3" fill="var(--red)"/></svg>
  </div>
  <div class="abs feature__ring" style="left:302px;top:378px">
    <svg width="40" height="28" viewBox="0 0 40 28"><rect x="2" y="3" width="36" height="22" rx="2" fill="none" stroke="var(--red)" stroke-width="3"/><rect x="7" y="7" width="26" height="14" rx="1" fill="var(--red)"/><circle cx="20" cy="14" r="5" fill="var(--white)"/><text x="20" y="17.5" text-anchor="middle" font-family="Oswald,sans-serif" font-size="9" font-weight="700" fill="var(--red)">1</text></svg>
  </div>
  <div class="abs feature__ring" style="left:469px;top:378px">
    <svg width="40" height="34" viewBox="0 0 40 34"><path d="M10 3h20l7 9-17 19L3 12z M3 12h34 M15 3l-4 9 9 19 9-19-4-9" fill="none" stroke="var(--red)" stroke-width="2.6" stroke-linejoin="round"/></svg>
  </div>
  <div class="abs feature__ring" style="left:666px;top:378px">
    <svg width="34" height="36" viewBox="0 0 34 36"><rect x="3" y="15" width="7" height="18" rx="1.5" fill="var(--red)"/><path d="M13 16l6-12c3 0 4 2 4 4l-1 6h8c2 0 3 2 3 4l-3 12c-1 2-2 3-4 3H13z" fill="var(--red)"/></svg>
  </div>

  <div class="abs feature__label" style="left:119px;top:432px">Experienced &amp; Friendly Professionals</div>
  <div class="abs feature__label" style="left:302px;top:432px">Free Estimates</div>
  <div class="abs feature__label" style="left:469px;top:432px">100% Satisfaction Guaranteed</div>
  <div class="abs feature__label" style="left:666px;top:432px">Residential &amp; Commercial</div>

  <div class="abs contact-row">
    <span class="contact-row__item">
      <svg width="14" height="22" viewBox="0 0 14 22"><path d="M9 1C5 1 2 5 2 11s3 10 7 10l2-4-3-2c-1-2-1-6 0-8l3-2-2-4z" fill="var(--blue)"/></svg>
      (555) 214-3870
    </span>
    <span class="contact-row__sep"></span>
    <span class="contact-row__item">
      <svg width="22" height="14" viewBox="0 0 22 14"><rect width="22" height="14" fill="var(--blue)"/><path d="M1 1l10 7 10-7" fill="none" stroke="var(--white)" stroke-width="1.5"/></svg>
      hello@brightlanewashco.com
    </span>
    <span class="contact-row__sep"></span>
    <span class="contact-row__item">
      <svg width="18" height="18" viewBox="0 0 18 18" fill="none" stroke="var(--blue)" stroke-width="1.5"><circle cx="9" cy="9" r="8"/><ellipse cx="9" cy="9" rx="3.5" ry="8"/><path d="M1 9h16M2.5 5h13M2.5 13h13"/></svg>
      www.brightlanewashco.com
    </span>
  </div>
</section>

<section class="card card--back" aria-label="Postcard back">
  <div class="abs back-left">
    <div class="abs strip"></div>
    <div class="abs gallery-band"></div>
    <div class="abs panel-top"></div>
    <div class="abs panel-bottom"></div>

    <div class="abs ribbon" style="top:30px">Residential Pressure Washing Services</div>
    <ul class="abs services" style="top:68px">
      <li>Soft Wash House Washing</li><li>Gutter Cleaning &amp; Brightening</li>
      <li>Driveway &amp; Concrete Cleaning</li><li>Deck &amp; Fence Washing</li>
    </ul>

    <div class="abs ribbon" style="top:126px">Commercial Pressure Washing Services</div>
    <ul class="abs services" style="top:163px">
      <li>Soft Wash Building Washing</li><li>Surface Cleaning</li>
      <li>Parking Lot Cleaning</li><li>Gum, Graffiti and Rust Removal</li>
    </ul>

    <div class="abs shot shot--before" style="left:106px;top:273px;background:linear-gradient(135deg,#8c8a5c,#c9c6a0)" role="img" aria-label="Before: stained house siding"></div>
    <div class="abs shot shot--before" style="left:228px;top:273px;background:linear-gradient(135deg,#c7a272,#6f7d45)" role="img" aria-label="Before: dirty gutter edge above grass"></div>
    <div class="abs shot shot--before" style="left:349px;top:273px;background:linear-gradient(135deg,#8f9290,#c9cbc8)" role="img" aria-label="Before: grimy concrete driveway"></div>
    <div class="abs shot shot--after" style="left:70px;top:353px;background:linear-gradient(135deg,#d9dfe6,#59624c)" role="img" aria-label="After: clean bright house siding"></div>
    <div class="abs shot shot--after" style="left:193px;top:353px;background:linear-gradient(135deg,#e3e5e2,#5f8a3c)" role="img" aria-label="After: clean gutter above grass"></div>
    <div class="abs shot shot--after" style="left:315px;top:353px;background:linear-gradient(135deg,#6d7d5a,#d6d6d1)" role="img" aria-label="After: clean concrete driveway"></div>

    <div class="abs tag" style="left:27px;top:263px">Before</div>
    <div class="abs tag" style="left:149px;top:263px">Before</div>
    <div class="abs tag" style="left:270px;top:263px">Before</div>
    <div class="abs tag" style="left:109px;top:378px">After</div>
    <div class="abs tag" style="left:230px;top:378px">After</div>
    <div class="abs tag" style="left:352px;top:378px">After</div>

    <svg class="abs" style="left:31px;top:282px" width="30" height="34" viewBox="0 0 30 34"><path d="M26 4C14 2 5 9 7 22l-5-1 8 12 6-13-5 1C9 12 15 7 26 4z" fill="var(--white)"/></svg>
    <svg class="abs" style="left:153px;top:282px" width="30" height="34" viewBox="0 0 30 34"><path d="M26 4C14 2 5 9 7 22l-5-1 8 12 6-13-5 1C9 12 15 7 26 4z" fill="var(--white)"/></svg>
    <svg class="abs" style="left:274px;top:282px" width="30" height="34" viewBox="0 0 30 34"><path d="M26 4C14 2 5 9 7 22l-5-1 8 12 6-13-5 1C9 12 15 7 26 4z" fill="var(--white)"/></svg>

    <div class="abs back-contact" style="top:436px">
      <svg width="9" height="16" viewBox="0 0 14 22"><path d="M9 1C5 1 2 5 2 11s3 10 7 10l2-4-3-2c-1-2-1-6 0-8l3-2-2-4z" fill="var(--blue)"/></svg>
      (555) 214-3870
    </div>
    <div class="abs back-contact" style="top:460px">
      <svg width="16" height="10" viewBox="0 0 22 14"><rect width="22" height="14" fill="var(--blue)"/><path d="M1 1l10 7 10-7" fill="none" stroke="var(--white)" stroke-width="1.5"/></svg>
      hello@brightlanewashco.com
    </div>
    <div class="abs back-contact" style="top:480px;letter-spacing:.6px">
      <svg width="12" height="12" viewBox="0 0 18 18" fill="none" stroke="var(--blue)" stroke-width="1.5"><circle cx="9" cy="9" r="8"/><ellipse cx="9" cy="9" rx="3.5" ry="8"/><path d="M1 9h16M2.5 5h13M2.5 13h13"/></svg>
      www.brightlanewashco.com
    </div>

    <div class="abs brand brand--back"><span class="brand__dot" style="width:11px;height:11px"></span>Brightlane Wash Co</div>
  </div>

  <div class="abs divider"></div>

  <div class="abs mail-address">
    <svg width="10" height="14" viewBox="0 0 10 14"><path d="M5 1a4 4 0 0 0-4 4c0 3 4 8 4 8s4-5 4-8a4 4 0 0 0-4-4z" fill="none" stroke="var(--red)" stroke-width="1.4"/><circle cx="5" cy="5" r="1.4" fill="var(--red)"/></svg>
    <div>Brightlane Wash Co<br>410 Harbor Palm Way<br>St Augustine, FL 32086</div>
  </div>
  <div class="abs stamp"></div>
  <div class="abs address-line" style="top:176px"></div>
  <div class="abs address-line" style="top:242px"></div>
  <div class="abs address-line" style="top:310px"></div>
  <div class="abs address-line" style="top:376px"></div>
</section>

</body>
</html>
```